LUMEN PI Planning Web App - Lean Agile at Scale - Distributed Big Room Planning Web & Touchscr...

We are the provider of the boardweave app http://boardweave-demo.example which currently is a desktop application. We are now working to bring all the features to a web-app but we don’t have a catchy design yet. The boardweave app is a visual collaboration tool for globally distributed teams and organization. Imagine a wall with lots of sticky notes on a flipchart hanging there – that’s basically our app just in a digital format. In general we want a light, modern, state of the art look and feel. Please take colorblind people into consideration when designing it.We are specifically looking for the following two design parts:- Design of the board structure- Sticky note designRequirements for the board structure- 16:9 ratio fixed- The board can be structured in 2 to 12 iterations + Risk Area and Objectives. Most common is 5 iterations + Risk Area and Objectives. Please go with the most common one but have in the back of your head that it needs to be compatible with 14 sections. Just for your imagination: in real life each of these areas on the board is one flip chart page.- Team Name: Somewhere on the board has to be the team name. It has to be easy to find and read.- In the iteration fields the user can set a velocity. That’s a simple numbers field. The load is calculated automatically and is just a number displayed on the board. There is an automatic visual indicator which should show with green or red colors if the teams are still in the plan. How this is brought to the attention is up to you.- Objectives & Stretch Objectives: The area with the Objectives is a list with text and a prioritization number attached to it. BV on the sketch stands for Business Value.Sticky Note design descriptionThe Sticky Note represents a physical sticky note or post-it note. When the user sees it he should instantly understand it as a sticky note and so for intuitively know what to do with it.Unselected sticky noteIf the sticky note is not selected it should be a simple sticky note sitting on the board.Following you find the things visible when the sticky note is not selected:- The sticky notes have a squared form factor- There is the text which is on the sticky note- In the upper right corner is a small sticky ID. Something like e.g. RT-4253.- Somewhere on the sticky note is also a number which should be easy to read. The numbers range from nothing over 0.5, 1, 2, 3, 5, 8, 13, 20, 40 up to 100.- Somewhere on the sticky needs to be a permanent text label. Not bigger than the rest of the text on the sticky note but easy to read.Selected sticky noteIf the user clicks on the sticky note once the following information needs to be displayed and he needs to be able to do the things listed and described below:- The sticky notes have a squared form factor- The user can write text on it- He can select different colors. These colors need to have a label so he knows what the function of these colors are.- By clicking a button he can add a flag to the sticky note- He can open a selection to choose the following number displayed on the sticky: 0.5, 1, 2, 3, 5, 8, 13, 20, 40, 100.- There is a delete sticky button. Place it where it makes sense from an intuitive stand point.- If he clicks the delete button, a short dialog appears on the sticky note: “Are you sure you want to delete this sticky note permanently? (It might delete an issue in your ALM tool)” He can confirm that by pressing “Delete” or “Cancel”.- In the upper right corner is a small sticky ID. Something like e.g. RT-4253.- Somewhere on or next to the sticky note needs to be a “sticky mirror” button as well as a “sticky move” button. Beside an optional icon for “mirror” and “move” there needs to be a naming tag so that everyone understands it right away.- It’s up to you to decide what’s the most intuitive way for the user.For better understanding also take a look at the rough sketch attached.

Font styles to use
Sans Serif

Requirements
Must have
• Color blind mode for different colored sticky notes

```html
<!DOCTYPE html>
<html lang="en">
<head>
<meta charset="utf-8">
<title>boardweave – Team Board</title>
<link rel="stylesheet" href="https://fonts.googleapis.com/css2?family=Roboto:wght@400;500;700&family=Roboto+Slab:wght@500&display=swap">
<style>
  :root{
    --top-green:#0fb80f;
    --title-gray:#707070;
    --obj-green:#0b5a2b;
    --bar-blue:#0a5fd0;
    --bar-blue-dark:#0745a5;
    --risk-red:#ee1b24;
    --panel-gray:#c9c9c9;
    --note-cream:#fffff0;
    --note-red:#ee1b24;
    --note-yellow:#dff02a;
    --tab-dark:#222;
    --tab-blue:#0b6fb5;
    --tab-green:#20a64a;
    --tab-red:#ee1b24;
    --select-green:#3e9d2e;
    --action-teal:#1aa0b8;
    --btn-green:#0d7a2e;
    --btn-black:#111;
    --btn-red:#ee1b24;
    --ink:#111;
    --white:#fff;
  }
  *{box-sizing:border-box;margin:0;padding:0}
  html,body{width:1200px;height:675px;overflow:hidden}
  body{font-family:"Roboto",Arial,sans-serif;position:relative;background:#ddd}
  .wall{position:absolute;inset:0;background:
      linear-gradient(100deg,#2f5a8c 0%,#3a6b9c 18%,#2aa39a 30%,#c9b07a 48%,#e5b94a 62%,#e9b53a 80%,#c77a2a 100%)}
  .topline{position:absolute;left:0;top:0;width:1200px;height:12px;background:var(--top-green)}
  .teambar{position:absolute;left:0;top:12px;width:1200px;height:28px;background:var(--title-gray);
    color:var(--white);font-size:15px;font-weight:500;line-height:28px;padding-left:34px;letter-spacing:.5px}
  .teambar::before{content:"";position:absolute;left:0;top:0;width:18px;height:28px;background:var(--top-green);
    clip-path:polygon(0 0,100% 0,60% 100%,0 100%)}

  .list{position:absolute;left:34px;width:172px;background:var(--white)}
  .list-head{height:24px;color:var(--white);font-size:10px;font-weight:700;letter-spacing:.6px;
    display:flex;justify-content:space-between;align-items:center;padding:0 12px;border-radius:8px 8px 0 0}
  .objectives{top:74px}
  .objectives .list-head{background:var(--obj-green)}
  .list-row{height:19px;background:var(--bar-blue);color:var(--white);font-family:"Roboto Slab",Georgia,serif;
    font-size:11px;display:flex;justify-content:space-between;align-items:center;padding:0 14px 0 10px;
    box-shadow:0 2px 3px rgba(0,0,0,.4);margin-top:4px}
  .list-row b{font-family:"Roboto",Arial,sans-serif;font-size:9px}
  .lines{position:relative;background:var(--white)}
  .lines span{position:absolute;left:6px;width:8px;height:8px;border-radius:50%;background:#d8d8d8;box-shadow:inset 1px 1px 2px #999}
  .risks{top:458px}
  .risks .list-head{background:var(--risk-red);justify-content:center;font-size:13px;height:26px}
  .risk-bar{height:18px;background:var(--bar-blue)}

  .iteration{position:absolute;width:272px}
  .iter-tab{height:17px;width:110px;background:var(--ink);color:var(--white);font-size:12px;font-weight:500;
    letter-spacing:.6px;padding-left:9px;line-height:17px;border-radius:0 12px 0 0}
  .iter-bar{height:16px;background:var(--bar-blue);display:flex;justify-content:flex-end;color:var(--white);
    font-size:12px;font-weight:700;letter-spacing:.4px;line-height:16px}
  .iter-bar .velocity{padding-right:16px;border-radius:0 10px 10px 0;background:var(--bar-blue);box-shadow:2px 0 0 #0a4fb0}
  .iter-bar .load{background:var(--bar-blue-dark);padding:0 10px 0 14px;margin-left:2px}
  .iter-body{height:228px;background:linear-gradient(180deg,#d4d4d4,#bdbdbd)}

  .sticky{position:absolute;width:64px;height:64px;background:var(--note);
    box-shadow:2px 3px 4px rgba(0,0,0,.45);border-top:8px solid var(--tab);border-radius:6px 6px 0 0}
  .sticky::before{content:attr(data-id);position:absolute;right:4px;top:-8px;font-size:6.5px;line-height:8px;color:var(--white)}
  .sticky.selected{outline:none}
  .select-frame{position:absolute;left:656px;top:240px;width:84px;height:80px;border-radius:8px;background:var(--select-green)}
  .quick-actions{position:absolute;left:750px;top:250px;list-style:none}
  .quick-actions li{display:flex;align-items:center;gap:3px;height:22px;font-size:5.5px;color:#222}
  .quick-actions i{width:15px;height:15px;border-radius:50%;background:var(--action-teal);display:block;position:relative}

  .action{position:absolute;text-align:center}
  .action-label{position:absolute;font-size:19px;letter-spacing:1.5px;color:var(--ink);white-space:nowrap}
  .action-btn{position:absolute;border-radius:50%;display:flex;align-items:center;justify-content:center}
</style>
</head>
<body>
  <div class="wall" role="img" aria-label="Painted brick wall backdrop in blue, teal and yellow tones"></div>
  <div class="topline"></div>
  <header class="teambar">TEAM NY</header>

  <section class="list objectives">
    <div class="list-head"><span>OBJECTIVES</span><span>BV</span></div>
    <div class="list-row"><span>My Objective</span><b>15</b></div>
    <div class="lines" style="height:138px">
      <span style="top:12px"></span><span style="top:38px"></span><span style="top:65px"></span><span style="top:91px"></span><span style="top:119px"></span>
    </div>
    <div class="list-row" style="margin-top:2px"><span>My Stretch</span><b>5</b></div>
    <div class="lines" style="height:152px">
      <span style="top:20px"></span><span style="top:50px"></span><span style="top:80px"></span><span style="top:105px"></span><span style="top:132px"></span>
    </div>
  </section>

  <section class="list risks">
    <div class="list-head">RISKS</div>
    <div class="risk-bar"></div>
    <div class="lines" style="height:128px;margin-top:2px">
      <span style="top:17px"></span><span style="top:40px"></span><span style="top:61px"></span><span style="top:82px"></span><span style="top:106px"></span>
    </div>
  </section>

  <section class="iteration" style="left:262px;top:77px">
    <div class="iter-tab">iteration 1.1</div>
    <div class="iter-bar"><span class="velocity">velocity 20</span><span class="load">Load&nbsp;&nbsp;5</span></div>
    <div class="iter-body" role="img" aria-label="Grey brick wall texture"></div>
  </section>
  <section class="iteration" style="left:558px;top:77px">
    <div class="iter-tab">iteration 1.1</div>
    <div class="iter-bar"><span class="velocity">velocity 20</span><span class="load">Load&nbsp;&nbsp;5</span></div>
    <div class="iter-body" role="img" aria-label="Grey brick wall texture"></div>
  </section>
  <section class="iteration" style="left:855px;top:77px">
    <div class="iter-tab">iteration 1.1</div>
    <div class="iter-bar"><span class="velocity">velocity 20</span><span class="load">Load&nbsp;&nbsp;5</span></div>
    <div class="iter-body" role="img" aria-label="Grey brick wall texture"></div>
  </section>
  <section class="iteration" style="left:262px;top:370px">
    <div class="iter-tab">iteration 1.1</div>
    <div class="iter-bar"><span class="velocity">velocity 20</span><span class="load">Load&nbsp;&nbsp;5</span></div>
    <div class="iter-body" role="img" aria-label="Grey brick wall texture"></div>
  </section>
  <section class="iteration" style="left:562px;top:370px">
    <div class="iter-tab">iteration 1.1</div>
    <div class="iter-bar"><span class="velocity">velocity 20</span><span class="load">Load&nbsp;&nbsp;5</span></div>
    <div class="iter-body" role="img" aria-label="Grey brick wall texture"></div>
  </section>

  <div class="select-frame"></div>

  <div class="sticky" data-id="RT 4321" style="left:294px;top:130px;--note:var(--note-cream);--tab:var(--tab-dark)"></div>
  <div class="sticky" data-id="RT 4321" style="left:397px;top:130px;--note:var(--note-red);--tab:var(--tab-dark)"></div>
  <div class="sticky" data-id="RT 4321" style="left:294px;top:226px;--note:var(--note-yellow);--tab:var(--tab-dark)"></div>
  <div class="sticky" data-id="RT 4321" style="left:456px;top:243px;--note:var(--note-red);--tab:var(--tab-blue)"></div>

  <div class="sticky" data-id="RT 4321" style="left:632px;top:156px;--note:var(--note-cream);--tab:var(--tab-blue)"></div>
  <div class="sticky" data-id="RT 4321" style="left:738px;top:130px;--note:var(--note-red);--tab:var(--tab-dark)"></div>
  <div class="sticky" data-id="RT 4321" style="left:574px;top:247px;--note:var(--note-yellow);--tab:var(--tab-dark)"></div>
  <div class="sticky selected" data-id="RT 4321" style="left:666px;top:247px;--note:var(--note-red);--tab:var(--tab-dark)"></div>

  <ul class="quick-actions">
    <li><i><svg width="15" height="15" viewBox="0 0 15 15"><path d="M5 5h5l-.6 6H5.6z M5.5 4h4" fill="#fff" stroke="#fff" stroke-width=".8"/></svg></i>Delete</li>
    <li><i><svg width="15" height="15" viewBox="0 0 15 15"><rect x="3.5" y="5" width="3" height="5" fill="#fff"/><rect x="8.5" y="5" width="3" height="5" fill="#fff"/></svg></i>Mirror</li>
    <li><i><svg width="15" height="15" viewBox="0 0 15 15"><rect x="4" y="4" width="4" height="7" fill="#fff"/><path d="M8.5 7.5h3M10 6l1.5 1.5L10 9" stroke="#fff" fill="none"/></svg></i>Move</li>
  </ul>

  <div class="sticky" data-id="RT 4321" style="left:887px;top:130px;--note:var(--note-yellow);--tab:var(--tab-green)"></div>
  <div class="sticky" data-id="RT 4321" style="left:1046px;top:130px;--note:var(--note-cream);--tab:var(--tab-blue)"></div>
  <div class="sticky" data-id="RT 4321" style="left:886px;top:250px;--note:var(--note-cream);--tab:var(--tab-dark)"></div>
  <div class="sticky" data-id="RT 4321" style="left:975px;top:247px;--note:var(--note-red);--tab:var(--tab-green)"></div>

  <div class="sticky" data-id="RT 4321" style="left:284px;top:415px;--note:var(--note-yellow);--tab:var(--tab-blue)"></div>
  <div class="sticky" data-id="RT 4321" style="left:378px;top:443px;--note:var(--note-cream);--tab:var(--tab-red)"></div>
  <div class="sticky" data-id="RT 4321" style="left:326px;top:557px;--note:var(--note-yellow);--tab:var(--tab-blue)"></div>
  <div class="sticky" data-id="RT 4321" style="left:460px;top:546px;--note:var(--note-cream);--tab:var(--tab-dark)"></div>

  <div class="sticky" data-id="RT 4321" style="left:574px;top:444px;--note:var(--note-cream);--tab:var(--tab-dark)"></div>
  <div class="sticky" data-id="RT 4321" style="left:726px;top:467px;--note:var(--note-yellow);--tab:var(--tab-blue)"></div>
  <div class="sticky" data-id="RT 4321" style="left:666px;top:546px;--note:var(--note-red);--tab:var(--tab-dark)"></div>

  <span class="action-label" style="left:1136px;top:427px">Move</span>
  <div class="action-btn" style="left:1124px;top:450px;width:72px;height:72px;background:var(--btn-green)">
    <svg width="40" height="36" viewBox="0 0 40 36"><rect x="2" y="2" width="22" height="32" fill="none" stroke="#fff" stroke-width="2"/>
      <path d="M6 8h14M6 12h14M6 16h14M6 20h14M6 24h14M6 28h14" stroke="#fff" stroke-width="1.6"/>
      <path d="M27 18h10M33 13l5 5-5 5" stroke="#fff" stroke-width="2.4" fill="none"/></svg>
  </div>

  <span class="action-label" style="left:1039px;top:475px">Mirror</span>
  <div class="action-btn" style="left:1038px;top:501px;width:72px;height:72px;background:var(--btn-black)">
    <svg width="52" height="28" viewBox="0 0 52 28"><rect x="1" y="1" width="18" height="26" fill="none" stroke="#fff" stroke-width="2"/>
      <rect x="33" y="1" width="18" height="26" fill="none" stroke="#fff" stroke-width="2"/>
      <path d="M4 7h12M4 11h12M4 15h12M4 19h12M4 23h12M36 7h12M36 11h12M36 15h12M36 19h12M36 23h12" stroke="#fff" stroke-width="1.5"/>
      <path d="M21 14h9M27 10l4 4-4 4" stroke="#fff" stroke-width="2" fill="none"/></svg>
  </div>

  <span class="action-label" style="left:977px;top:565px">Delete</span>
  <div class="action-btn" style="left:975px;top:591px;width:74px;height:74px;background:var(--btn-red)">
    <svg width="26" height="34" viewBox="0 0 26 34"><path d="M3 8h20l-2.5 25h-15z" fill="#fff"/><path d="M2 4l22 2-1 2-22-2z M9 3l1-3h6l1 3" fill="#fff"/></svg>
  </div>
</body>
</html>
```